Modern card design needed for building development company

We are looking for a sharp modern new look for our business cards.
We are a New Zealand based company called TKV Ventures NZ LTD that specialises in subdividing large sections, housing and commercial buildings.
We have attached a photo of the current logo and would like to see it improved somehow as it looks a bit dated.
We are open to any colours.

Target Market(s)

Investors, Property buyers

Industry/Entity Type

Investment

Contact Information for Business Card

TKV VENTURES NZ LTD
www.tkvventuresnz.co.nz

Howard Pennick
Phone +64 21 843 192
Email hdpennick@fernmail.co.nz

Font styles to use
Serif
Sans Serif

Colors
0792cd
33a6d7
85cae6
6b449b
886aae
f04a50
ec1f27
f37122
f68d4d

Requirements
Must have
• Please try and make the logo more modern or if you have a similar one we would like to see it.

```html
<!DOCTYPE html>
<html lang="en">
<head>
<meta charset="utf-8">
<title>TKV Ventures NZ LTD – Business Card</title>
<link rel="stylesheet" href="https://fonts.googleapis.com/css2?family=Montserrat:wght@700&family=Open+Sans:wght@300;400&display=swap">
<style>
  :root {
    --page: #e9e6e2;
    --card-dark: #2b2b2d;
    --card-dark-edge: #222224;
    --blue: #0792cd;
    --blue-mid: #33a6d7;
    --blue-light: #85cae6;
    --text-light: #e4e6e8;
    --text-muted: #b9bcc0;
  }
  * { margin: 0; padding: 0; box-sizing: border-box; }
  html, body { width: 1200px; height: 1000px; overflow: hidden; }
  body {
    background: var(--page);
    position: relative;
    font-family: "Open Sans", Arial, sans-serif;
  }
  .card {
    position: absolute;
    width: 760px;
    height: 434px;
    background: radial-gradient(ellipse at 40% 35%, var(--card-dark) 0%, var(--card-dark-edge) 100%);
    overflow: hidden;
    box-shadow: 0 6px 18px rgba(0,0,0,0.18);
  }
  .card--front { left: 60px; top: 50px; }
  .card--back { left: 380px; top: 516px; }

  /* front */
  .accent-line {
    position: absolute;
    height: 8px;
    background: linear-gradient(90deg, var(--blue), var(--blue-mid));
  }
  .accent-line--left { left: 110px; width: 250px; top: 268px; }
  .accent-line--right { left: 478px; width: 282px; top: 182px; }
  .brand {
    position: absolute;
    left: 0; right: 0;
    top: 196px;
    text-align: center;
  }
  .brand__mark {
    display: inline-block;
    width: 22px; height: 22px;
    background: var(--blue-mid);
    vertical-align: middle;
    margin-right: 10px;
  }
  .brand__name {
    font-family: "Montserrat", Arial, sans-serif;
    font-weight: 700;
    font-size: 25px;
    color: var(--text-light);
    vertical-align: middle;
    letter-spacing: 0.5px;
  }
  .website {
    position: absolute;
    left: 0; right: 0;
    top: 296px;
    text-align: center;
    font-size: 16px;
    color: var(--text-muted);
    letter-spacing: 0.6px;
  }

  /* back */
  .corner-triangle { position: absolute; left: 0; top: 0; }
  .building-panel { position: absolute; right: 0; top: 0; }
  .divider {
    position: absolute;
    left: 480px; top: 195px;
    width: 2px; height: 150px;
    background: var(--blue);
  }
  .contact {
    position: absolute;
    right: 300px;
    top: 190px;
    text-align: right;
  }
  .contact__name {
    font-size: 30px;
    font-weight: 300;
    color: var(--text-light);
    letter-spacing: 0.5px;
    line-height: 1;
  }
  .contact__first {
    font-family: "Montserrat", Arial, sans-serif;
    font-weight: 700;
    color: var(--blue);
  }
  .contact__role {
    font-size: 15px;
    color: var(--text-muted);
    margin-top: 6px;
  }
  .contact__list { list-style: none; margin-top: 34px; }
  .contact__item {
    font-size: 15px;
    color: var(--text-light);
    margin-bottom: 14px;
    display: flex;
    justify-content: flex-end;
    align-items: center;
    gap: 8px;
  }
  .contact__icon { width: 14px; height: 14px; flex: none; }
</style>
</head>
<body>

<section class="card card--front" aria-label="Card front">
  <div class="accent-line accent-line--right"></div>
  <div class="brand">
    <span class="brand__mark"></span><span class="brand__name">TKV VENTURES NZ LTD</span>
  </div>
  <div class="accent-line accent-line--left"></div>
  <p class="website">www.tkvventuresnz.co.nz</p>
</section>

<section class="card card--back" aria-label="Card back">
  <svg class="corner-triangle" width="420" height="200" viewBox="0 0 420 200">
    <defs>
      <linearGradient id="triBlue" x1="0" y1="0" x2="1" y2="1">
        <stop offset="0" stop-color="#33a6d7"/>
        <stop offset="1" stop-color="#0792cd"/>
      </linearGradient>
    </defs>
    <polygon points="0,0 410,0 0,190" fill="url(#triBlue)"/>
  </svg>

  <svg class="building-panel" width="270" height="434" viewBox="0 0 270 434" role="img" aria-label="Blue striped building motif">
    <defs>
      <linearGradient id="panelBlue" x1="0" y1="0" x2="1" y2="1">
        <stop offset="0" stop-color="#85cae6"/>
        <stop offset="1" stop-color="#0792cd"/>
      </linearGradient>
    </defs>
    <rect x="0" y="0" width="270" height="434" fill="url(#panelBlue)"/>
  </svg>

  <div class="divider"></div>

  <div class="contact">
    <p class="contact__name"><span class="contact__first">HOWARD</span> PENNICK</p>
    <p class="contact__role">Position</p>
    <ul class="contact__list">
      <li class="contact__item">+64 21 843 192
        <svg class="contact__icon" viewBox="0 0 14 14" aria-hidden="true"><rect x="3" y="0.5" width="8" height="13" rx="1.5" fill="none" stroke="#33a6d7" stroke-width="1.4"/><circle cx="7" cy="11" r="0.9" fill="#33a6d7"/></svg>
      </li>
      <li class="contact__item">hdpennick@fernmail.co.nz
        <svg class="contact__icon" viewBox="0 0 14 14" aria-hidden="true"><rect x="0.7" y="2.5" width="12.6" height="9" fill="none" stroke="#33a6d7" stroke-width="1.4"/><polyline points="0.7,2.5 7,8 13.3,2.5" fill="none" stroke="#33a6d7" stroke-width="1.4"/></svg>
      </li>
    </ul>
  </div>
</section>

</body>
</html>
```